RV Wrecking business cards v.2 first was me

So the ones in the picture are my original cards that I came up with. 😅however I kinda messed up on two things, I missed spelled my name it should be Dariel Montoya as well as the email should be Darielm@brightlanecrews.com. I would like to clean this card up and also make it pop! Something that people would remember me by and that screams DEMOLITION. As well as a card that give you a feeling of loyalty and trust. I would also like to change and remove junk hauling and add full demolition to replace it. These cards worked for a little while but I cant make that my image while handing these out. I would also like to only put down that we are located in Mesa Verde Hills, CA, 92675 instead of the address on the card. Also if we can have a line that states Licensed, Bonded, & Insured. With out License # 4837215

Target Market(s)

Contractors and Home owners

Industry/Entity Type

Construction specialist in Demolition

Contact Information for Business Card

R Wrecking Selective Demolition & Full Demolition Kitchens AD Preparation Bathrooms Sheds Interiors & Exteriors Demo Digging And Much More Darielll Montoya Owner our city state and zip

Font styles to use
Serif
Sans Serif
Decorative

Colors
0054AA
0677BA
7BADD7
CADEEF
E8F1F8
0094D4
00A9DD
6FCCEA
C7EBF8
E9F6FB

Requirements
Must have
• License# 4837215
Nice to have
• Trying to go with a blue and white color scheme
Should not have
• Building construction

```html
<!DOCTYPE html>
<html lang="en">
<head>
<meta charset="utf-8">
<title>RV Wrecking – Business Cards</title>
<link rel="stylesheet" href="https://fonts.googleapis.com/css2?family=Lato:wght@400;700;900&display=swap">
<style>
  :root {
    --stage: #2e2e30;
    --brand-blue: #0f4f99;
    --card-white: #ffffff;
    --ink: #000000;
    --text-light: #ffffff;
  }
  * { box-sizing: border-box; margin: 0; padding: 0; }
  html, body { width: 1200px; height: 875px; overflow: hidden; }
  body {
    background: var(--stage);
    font-family: "Lato", sans-serif;
    position: relative;
  }
  .card {
    position: absolute;
    width: 560px;
    height: 320px;
    border-radius: 18px;
    overflow: hidden;
  }

  /* Front card */
  .card-front {
    left: 40px; top: 90px;
    background: var(--brand-blue);
    color: var(--text-light);
  }
  .front-title {
    position: absolute; left: 34px; top: 56px;
    font-weight: 900; font-size: 40px; letter-spacing: 1px; line-height: 1;
  }
  .front-tagline {
    position: absolute; left: 36px; top: 102px;
    font-size: 16.5px; font-weight: 400;
  }
  .front-rule {
    position: absolute; left: 36px; top: 134px;
    width: 62px; height: 2px; background: var(--text-light);
  }
  .service-list {
    position: absolute; left: 40px; top: 146px;
    list-style: none; font-size: 15.5px; line-height: 21px;
  }
  .service-list li::before {
    content: ""; display: inline-block;
    width: 8px; height: 8px; border-radius: 50%;
    background: var(--text-light); margin-right: 10px; vertical-align: 2px;
  }
  .front-brand {
    position: absolute; right: 28px; top: 186px;
    display: flex; align-items: center; gap: 12px;
    font-weight: 900; font-size: 36px; line-height: 1;
    white-space: nowrap;
  }
  .front-brand .mark-square {
    width: 26px; height: 26px; background: var(--text-light);
  }

  /* Back card */
  .card-back {
    left: 600px; top: 465px;
    background: var(--card-white);
  }
  .back-brand {
    position: absolute; left: 120px; top: 44px;
    display: flex; align-items: center; gap: 12px;
    color: var(--brand-blue); font-weight: 900; font-size: 40px; line-height: 1;
  }
  .back-brand .mark-square {
    width: 24px; height: 24px; background: var(--brand-blue);
  }
  .license {
    position: absolute; left: 300px; top: 92px;
    font-weight: 900; font-size: 14px; letter-spacing: 0.5px; color: var(--ink);
  }
  .info-band {
    position: absolute; left: 0; top: 132px;
    width: 100%; height: 100px; display: flex;
  }
  .name-panel {
    width: 56%; background: var(--ink); color: var(--text-light);
    display: flex; flex-direction: column; justify-content: center;
    padding-left: 40px;
  }
  .owner-name {
    font-weight: 900; font-size: 27px; letter-spacing: 1px; text-transform: uppercase;
  }
  .owner-role { font-size: 15px; margin-top: 2px; align-self: flex-end; margin-right: 24px; }
  .contact-panel {
    width: 44%; background: var(--brand-blue); color: var(--text-light);
    list-style: none; padding: 18px 0 0 16px; font-size: 12.5px; line-height: 21px;
  }
  .contact-panel li { display: flex; align-items: center; gap: 8px; white-space: nowrap; }
  .contact-panel svg { width: 12px; height: 12px; fill: var(--text-light); flex: none; }
  .credentials {
    position: absolute; left: 0; right: 0; top: 256px;
    text-align: center; color: var(--brand-blue);
    font-weight: 900; font-size: 16px; letter-spacing: 0.5px;
  }
</style>
</head>
<body>

<section class="card card-front" aria-label="Card front">
  <h1 class="front-title">R WRECKING</h1>
  <p class="front-tagline">Selective Demolition &amp; Full Demolition</p>
  <div class="front-rule"></div>
  <ul class="service-list">
    <li>Kitchens</li>
    <li>ADU Preparation</li>
    <li>Bathrooms</li>
    <li>Sheds</li>
    <li>Interiors &amp; Exteriors Demo</li>
    <li>Digging &amp; Much More</li>
  </ul>
  <div class="front-brand"><span class="mark-square"></span>RV Wrecking</div>
</section>

<section class="card card-back" aria-label="Card back">
  <div class="back-brand"><span class="mark-square"></span>RV Wrecking</div>
  <p class="license">LICENSE# 4837215</p>
  <div class="info-band">
    <div class="name-panel">
      <p class="owner-name">Dariel Montoya</p>
      <p class="owner-role">Owner</p>
    </div>
    <ul class="contact-panel">
      <li>
        <svg viewBox="0 0 24 24" aria-hidden="true"><path d="M6.6 10.8a15 15 0 0 0 6.6 6.6l2.2-2.2a1 1 0 0 1 1-.25 11.4 11.4 0 0 0 3.6.57 1 1 0 0 1 1 1V20a1 1 0 0 1-1 1A17 17 0 0 1 3 4a1 1 0 0 1 1-1h3.5a1 1 0 0 1 1 1c0 1.25.2 2.45.57 3.6a1 1 0 0 1-.25 1z"/></svg>
        (555)318-2047
      </li>
      <li>
        <svg viewBox="0 0 24 24" aria-hidden="true"><path d="M2 5h20v14H2z M2 5l10 8 10-8" /></svg>
        Darielm@brightlanecrews.com
      </li>
      <li>
        <svg viewBox="0 0 24 24" aria-hidden="true"><path d="M12 2a7 7 0 0 0-7 7c0 5 7 13 7 13s7-8 7-13a7 7 0 0 0-7-7zm0 9.5A2.5 2.5 0 1 1 12 6.5a2.5 2.5 0 0 1 0 5z"/></svg>
        Mesa Verde Hills, CA, 92675
      </li>
    </ul>
  </div>
  <p class="credentials">LICENSED, BONDED, &amp; INSURED</p>
</section>

</body>
</html>
```